Packaging design for handmade soap

We are looking for a packaging design for a brand new product line: handmade soaps, called BRIVO

We are looking for a design of an outer box together with the logo. We need the design for a 90x65x30mm box (see attached). We trying to get a high-end product preferable with vintage elements (but we don't want a shiny box, it will be finished with matte lacque, however logo or other certain elements could be shiny).

The design should reflect the fact that we have a handmade, all natural soap.

I uploaded a couple of packaging examples I like.

UPDATE 1: It also should have a title, which describes the product more accurate, like "Natural Soap with Seabuckthorn and Olive oil"

UPDATE 2: I would remove the expression "high-end" from the description if high end would mean a lot of flowers in the background. I would like if you would insist about the ideea of "natural" in your works

UPDATE 3: Prefered colors green and brown (which brings the ideea of nature, natural)

Target Market(s)

Women 20-45 years with above average income

Industry/Entity Type

Cosmetics

Font styles to use
Serif

Colors
9bcb3c
acd036
cadf82
f78f20
ffc214
f37122
fbed22
fece3e
faa54b

Requirements
Must have
• A literal representation of the brand BRIVO (we don't have a logo for it)

```html
<!DOCTYPE html>
<html lang="en">
<head>
<meta charset="utf-8">
<title>BRIVO Handmade Soaps – Box Front</title>
<link href="https://fonts.googleapis.com/css2?family=Libre+Baskerville:wght@400;700&family=Lato:wght@400&display=swap" rel="stylesheet">
<style>
  :root {
    --page: #ffffff;
    --linen: #c9c9a1;
    --linen-light: #d6d5b2;
    --ink: #5b4630;
    --ornament: #a89a78;
    --ribbon: #cb6858;
    --ribbon-text: #e9dfb2;
  }
  * { margin: 0; padding: 0; box-sizing: border-box; }
  html, body {
    width: 1200px; height: 902px; overflow: hidden;
    background: var(--page);
  }
  .box-front {
    position: absolute;
    left: 188px; top: 152px;
    width: 830px; height: 600px;
    background: radial-gradient(ellipse at center, var(--linen-light) 0%, var(--linen) 80%);
    box-shadow: 2px 2px 3px rgba(0,0,0,0.35);
  }
  .ornament {
    position: absolute;
    background: radial-gradient(ellipse at center, rgba(120,100,70,0.35) 0%, rgba(120,100,70,0.08) 70%, transparent 100%);
  }
  .ornament--corner { width: 232px; height: 208px; }
  .ornament--tl { left: 12px; top: 12px; }
  .ornament--tr { right: 12px; top: 12px; }
  .ornament--bl { left: 12px; bottom: 12px; }
  .ornament--br { right: 12px; bottom: 12px; }
  .ornament--rosette { width: 64px; height: 44px; top: 268px; }
  .ornament--left { left: 4px; }
  .ornament--right { right: 4px; }

  .brand {
    position: absolute; left: 0; right: 0; top: 102px;
    text-align: center;
    font-family: "Libre Baskerville", serif;
    font-weight: 400;
    font-size: 94px;
    line-height: 1;
    letter-spacing: 2px;
    color: var(--ink);
  }
  .brand-line {
    position: absolute; left: 0; right: 0; top: 202px;
    text-align: center;
    font-family: "Lato", sans-serif;
    font-size: 31px;
    letter-spacing: 4px;
    color: var(--ink);
  }
  .product-title {
    position: absolute; left: 0; right: 0; top: 297px;
    text-align: center;
    font-family: "Libre Baskerville", serif;
    font-weight: 700;
    font-size: 44px;
    letter-spacing: 9px;
    color: var(--ink);
  }
  .ribbon {
    position: absolute; left: 150px; top: 366px;
    width: 520px; height: 84px;
  }
  .ribbon svg { position: absolute; inset: 0; }
  .ribbon-text {
    position: absolute; inset: 0;
    display: flex; flex-direction: column; justify-content: center; align-items: center;
    font-family: "Libre Baskerville", serif;
    font-weight: 700;
    font-size: 25px;
    line-height: 36px;
    letter-spacing: 3px;
    color: var(--ribbon-text);
  }
  .weight {
    position: absolute; left: 0; right: 0; top: 534px;
    text-align: center;
    font-family: "Libre Baskerville", serif;
    font-size: 27px;
    color: var(--ink);
  }
</style>
</head>
<body>
  <main class="box-front">
    <div class="ornament ornament--corner ornament--tl" role="img" aria-label="Vintage floral scroll ornament"></div>
    <div class="ornament ornament--corner ornament--tr" role="img" aria-label="Vintage floral scroll ornament"></div>
    <div class="ornament ornament--corner ornament--bl" role="img" aria-label="Vintage floral scroll ornament"></div>
    <div class="ornament ornament--corner ornament--br" role="img" aria-label="Vintage floral scroll ornament"></div>
    <div class="ornament ornament--rosette ornament--left" role="img" aria-label="Small floral rosette"></div>
    <div class="ornament ornament--rosette ornament--right" role="img" aria-label="Small floral rosette"></div>

    <h1 class="brand">BRIVO</h1>
    <p class="brand-line">HANDMADE SOAPS</p>

    <h2 class="product-title">NATURAL SOAP</h2>

    <div class="ribbon">
      <svg width="520" height="84" viewBox="0 0 520 84" aria-hidden="true">
        <polygon points="10,0 520,0 510,84 0,84" fill="var(--ribbon)"/>
      </svg>
      <p class="ribbon-text"><span>With Seabuckthorn</span><span>&amp; Olive oil</span></p>
    </div>

    <p class="weight">4oz/100g</p>
  </main>
</body>
</html>
```